Managed IT services business card design

We haven't needed a business card since the founding of the business in 2005. All our clients have been coming through word of mouth. And lately more and more existing clients are requesting for our business cards to pass on to their contacts in recommending us.
So we needing a business card design. We use various innovative solutions and methodologies to provide IT services to small businesses in managing their IT systems. Our role is the same as an in-house, full-time IT Manager for our clients, but outsourced. So we take care of all our clients' IT needs, just as an IT Manager would be expected to perform.
We have a holding website, which we're happy to leave for now. If we can use the same logo would be great - www.tegvu.com.au
Preferred colours are shades of are white, grey and black.
We pride our business with the following traits: proactive, good service, prompt response, trustworthy.
Target Market(s)
Small businesses of any industry
Industry/Entity Type
Business

```html
<!DOCTYPE html>
<html lang="en">
<head>
<meta charset="utf-8">
<title>tegvu — Business Card</title>
<link href="https://fonts.googleapis.com/css2?family=Questrial&display=swap" rel="stylesheet">
<style>
  :root {
    --backdrop: #5a4330;
    --card-top: #ffffff;
    --card-bottom: #e6e6e6;
    --ink: #1a1a1a;
    --ink-soft: #3c3c3c;
    --ink-muted: #9a9a9a;
    --shadow: rgba(0, 0, 0, 0.45);
  }
  * { margin: 0; padding: 0; box-sizing: border-box; }
  html, body {
    width: 1200px;
    height: 900px;
    overflow: hidden;
    background: var(--backdrop);
    font-family: "Questrial", "Century Gothic", sans-serif;
  }
  .business-card {
    position: absolute;
    left: 100px;
    top: 164px;
    width: 1000px;
    height: 572px;
    background: linear-gradient(180deg, var(--card-top) 0%, var(--card-top) 45%, var(--card-bottom) 100%);
    box-shadow: 0 18px 40px var(--shadow);
    color: var(--ink);
  }
  .brand {
    position: absolute;
    left: 0;
    width: 100%;
    top: 100px;
    display: flex;
    justify-content: center;
    align-items: center;
    gap: 22px;
  }
  .brand-name {
    font-size: 80px;
    line-height: 1;
    color: var(--ink);
  }
  .brand-dot {
    width: 30px;
    height: 30px;
    border-radius: 50%;
    background: var(--ink);
  }
  .holder {
    position: absolute;
    left: 0;
    width: 100%;
    top: 205px;
    text-align: center;
  }
  .holder-name {
    font-size: 32px;
    line-height: 1.1;
    color: var(--ink);
  }
  .holder-title {
    font-size: 17px;
    letter-spacing: 0.05em;
    color: var(--ink-muted);
  }
  .address {
    position: absolute;
    left: 280px;
    top: 350px;
    font-size: 21px;
    color: var(--ink);
    white-space: nowrap;
  }
  .online {
    position: absolute;
    left: 680px;
    top: 270px;
    font-size: 21px;
    line-height: 1.45;
    color: var(--ink);
    white-space: nowrap;
  }
  .phones {
    position: absolute;
    left: 60px;
    top: 445px;
    font-size: 23px;
    line-height: 1.45;
    color: var(--ink-soft);
  }
</style>
</head>
<body>
  <main class="business-card">
    <div class="brand">
      <span class="brand-name">tegvu</span>
      <span class="brand-dot"></span>
    </div>
    <div class="holder">
      <div class="holder-name">Daniel Hart</div>
      <div class="holder-title">CEO</div>
    </div>
    <div class="address">48 Orion Lane Northbay 2100 Sydney</div>
    <div class="online">
      <div class="email">Email: tegvu@mailbox.com</div>
      <div class="web">Web: www.tegvu.com.au</div>
    </div>
    <div class="phones">
      <div class="tel">Tel: 877.555.0142</div>
      <div class="fax">Fax: 877.555.0143</div>
    </div>
  </main>
</body>
</html>
```